Van wrap design based on business card

Hi folks, I need a clean design van wrap for Corvane Van 2008 Hightop using existing business card details and design. Also need to include (small subtle) velmora and torquelane logo.

Roving Spoke Fixers -
The actual van is white. Van is Kestra Corvane 2008 Hightop roof.

Please keep the design simple, use the business card for style - design must complete or be the same as the business card.

We dont want to wrap the entire vehicle - using the spot colours only and so it can be easily found from a distance in a busy car park or at a race.

Need artwork file ready for laser cutting Thanks very much

Target Market(s)

25-40 years of age - triathletes/roadbikers

Industry/Entity Type

Mechanic

Font styles to use
Other font styles liked:
• Arial or roboto

Requirements
Must have
• Spot colour - 361PC Green Black and white
• Contact details must be included in the design - phone number is MOST important.
• Graphics on actual van (not substitution or different make.)
Nice to have
• Clean modern design
Should not have
• Photos or new style of design.

```html
<!DOCTYPE html>
<html lang="en">
<head>
<meta charset="utf-8">
<title>Roving Spoke Fixers – Corvane Rear Door Wrap</title>
<link rel="stylesheet" href="https://fonts.googleapis.com/css2?family=Roboto:wght@400;500;700&display=swap">
<style>
  :root {
    --spot-green: #5aa347;
    --wrap-charcoal: #3b3b3c;
    --wrap-white: #ffffff;
    --stage: #eeeeee;
  }
  html, body {
    margin: 0;
    padding: 0;
    width: 1200px;
    height: 822px;
    overflow: hidden;
    background: var(--stage);
  }
  .wrap-canvas {
    display: block;
    width: 1200px;
    height: 822px;
  }
  .door-panel { fill: var(--wrap-charcoal); }
  .spot-band { fill: var(--spot-green); }
  .arrow-outline { fill: var(--wrap-white); }
  .arrow-fill { fill: var(--spot-green); }
  .headline, .tagline, .service-item {
    font-family: "Roboto", Arial, sans-serif;
  }
  .headline { font-weight: 500; font-size: 40px; }
  .headline--green { fill: var(--spot-green); }
  .headline--white { fill: var(--wrap-white); font-size: 32px; }
  .service-item { fill: var(--wrap-white); font-weight: 400; font-size: 21px; }
  .service-star { fill: var(--spot-green); }
  .tagline { font-weight: 500; font-size: 30px; text-anchor: middle; }
  .tagline--green { fill: var(--spot-green); }
  .tagline--white { fill: var(--wrap-white); }
</style>
</head>
<body>
<svg class="wrap-canvas" viewBox="0 0 1200 822" xmlns="http://www.w3.org/2000/svg">
  <defs>
    <clipPath id="door-shape">
      <path d="M376,86 Q592,62 808,86 Q890,150 918,430 L915,700 Q914,740 905,748 L292,748 Q280,740 278,700 L270,430 Q298,150 376,86 Z"/>
    </clipPath>
    <symbol id="star" viewBox="-10 -10 20 20">
      <path d="M0,-9.5 L2.8,-3.2 L9.5,-2.9 L4.4,1.5 L5.9,8.5 L0,4.8 L-5.9,8.5 L-4.4,1.5 L-9.5,-2.9 L-2.8,-3.2 Z"/>
    </symbol>
  </defs>

  <g class="rear-door" clip-path="url(#door-shape)">
    <rect class="door-panel" x="260" y="50" width="680" height="720"/>
    <polygon class="arrow-outline" points="768,266 882,218 930,350"/>
    <polygon class="arrow-fill" points="800,268 882,234 930,330"/>
    <rect class="spot-band" x="260" y="676" width="680" height="80"/>
  </g>

  <g class="headline-block">
    <text class="headline headline--green" x="430" y="145" textLength="330" lengthAdjust="spacingAndGlyphs">MOBILE SERVICING</text>
    <text class="headline headline--white" x="430" y="183" textLength="328" lengthAdjust="spacingAndGlyphs">&amp; REPAIR SPECIALISTS</text>
  </g>

  <g class="service-list">
    <use class="service-star" href="#star" x="430" y="214" width="19" height="19"/>
    <text class="service-item" x="462" y="230">Race preparation &amp; wheel hire</text>
    <use class="service-star" href="#star" x="430" y="254" width="19" height="19"/>
    <text class="service-item" x="462" y="270">Bike boxing services</text>
    <use class="service-star" href="#star" x="430" y="296" width="19" height="19"/>
    <text class="service-item" x="462" y="312">New bikes &amp; accessories</text>
    <use class="service-star" href="#star" x="430" y="336" width="19" height="19"/>
    <text class="service-item" x="462" y="352">Velmora certified</text>
  </g>

  <g class="tagline-block">
    <text class="tagline tagline--green" x="598" y="408" textLength="286" lengthAdjust="spacingAndGlyphs">WE LOVE YOUR BIKE</text>
    <text class="tagline tagline--white" x="598" y="445" textLength="432" lengthAdjust="spacingAndGlyphs">ALMOST AS MUCH AS YOU DO!</text>
  </g>
</svg>
</body>
</html>
```